Website Update for Global Company - Solar Technology - Brisqell

We recently released our first version of our website kelvaris.com. However despite a longer process of developing the page, it is still missing the elements of a brilliant website. (Currently it looks dead and boring) We are having problems integrating our logo and want to create a more catching site. The task involves an updated and without changing most of main elements in the existing page. (Unless you can do it even better) The blue color needs to be kept but can be changed within the blue-spectrum. The logo text (KELVARIS) must be better integrated in the site, however the main logo could be used in elements like we have tried with the background. The surface of the logo could be changed to 3D or metallic, or any other theme that would make the site more complete.
It would be good if some elements of the site could be used on business cards and invoices to keep the company identity.
Kelvaris is a new development company specialized in green energy and sustainable development. We do design, engineering, manufacturing, sourcing and other processes related to product development – both as consultants and for own products.
Keep the look of the site as professional as possible, and with a cooperate-looking style.

Link to existing page: www.kelvaris.com

Brief Update : After reviewing the designs we would like all new and current designers to make more bold designs that stands out from the rest. We do not like the standard layout that looks like any other cooperate homepage. We want a very unique and very lively page - with faded images and effects when hoovering like seen on our existing page. Try make all elements blend together, and use faded background images instead of just white color - or something else.

Make the site unique !

Industry/Entity Type

Solar Energy

Contact Information for Business Card

Owner/Founder/CEO : Frederik Lysgaard Holm
Company name: Kelvaris ApS
Email: frederik.lysgaard@kelvaris.dk
Phone: +45 71 83 96 54
Slogan Sustainable Development
Address: Havnestien 18, 2
DK-5820 Svendborg, Denmark

Number of Pages Required

3 page

Font styles to use
Serif
Sans Serif

Colors
0555a3
85acd3
cedeed
3176b5
cee9f5
85cae6
0293ce
86cfc6
33b8a4

```html
<!DOCTYPE html>
<html lang="en">
<head>
<meta charset="utf-8">
<title>Kelvaris – Sustainable Development</title>
<link href="https://fonts.googleapis.com/css2?family=Open+Sans:wght@400;600;700;800&family=Montserrat:wght@600;700&display=swap" rel="stylesheet">
<style>
:root{
  --navy:#0b2c5c;
  --deep:#0555a3;
  --mid:#3176b5;
  --sky:#85acd3;
  --pale:#cedeed;
  --ice:#cee9f5;
  --cyan:#0293ce;
  --ink:#333b45;
  --muted:#6b7480;
  --white:#ffffff;
}
*{box-sizing:border-box;margin:0;padding:0}
html,body{width:1200px;height:3132px;overflow:hidden}
body{font-family:"Open Sans",Arial,sans-serif;color:var(--ink);background:var(--white);position:relative}
.abs{position:absolute}

/* top bar */
.topbar{left:0;top:0;width:1200px;height:40px;background:var(--navy);color:#cfe0f3;font-size:12px;display:flex;align-items:center;gap:26px;padding-left:160px}
.topbar span{display:flex;align-items:center;gap:6px}

/* header */
.header{left:0;top:40px;width:1200px;height:128px;background:var(--white)}
.logo{display:flex;align-items:center;gap:14px}
.logo-mark{width:52px;height:52px;background:var(--deep)}
.logo-name{font-family:"Montserrat",sans-serif;font-weight:700;font-size:34px;letter-spacing:4px;color:var(--navy);line-height:1}
.logo-tag{font-size:10px;letter-spacing:3px;color:var(--muted);margin-top:4px}
.header .logo{position:absolute;left:160px;top:36px}
.nav{position:absolute;right:160px;top:44px;display:flex;gap:4px}
.nav a{font-size:13px;font-weight:600;color:var(--deep);text-decoration:none;padding:10px 14px}
.nav a.active{background:var(--deep);color:var(--white)}

/* hero */
.hero{left:0;top:168px;width:1200px;height:500px;background:linear-gradient(180deg,#2c6fb8 0%,#5da0dc 40%,#0d3f86 75%,#153a70 100%)}
.hero-box{position:absolute;left:160px;top:130px;width:540px;padding:28px 30px;background:rgba(5,85,163,.82);color:var(--white);font-family:"Montserrat",sans-serif;font-weight:700;font-size:26px;line-height:1.3;letter-spacing:.5px}
.hero-cut{position:absolute;left:0;bottom:0}

/* section heads */
.sec-title{display:flex;align-items:center;justify-content:center;gap:14px;font-family:"Montserrat",sans-serif;font-weight:600;font-size:24px;letter-spacing:2px}
.sec-title::before,.sec-title::after{content:"";width:60px;height:2px;background:currentColor}
.body-copy{font-size:13px;line-height:1.75;color:var(--muted);text-align:center}

.welcome{left:0;top:668px;width:1200px;height:272px;background:linear-gradient(180deg,#fff 0%,#f3f8fc 100%)}
.welcome .sec-title{color:var(--navy);margin-top:70px}
.welcome .body-copy{width:880px;margin:26px auto 0}

/* featured */
.featured{left:0;top:900px;width:1200px;height:580px;background:linear-gradient(180deg,#0c4d9c,#0555a3 55%,#0a3f80);clip-path:polygon(0 9%,100% 0,100% 88%,0 100%)}
.featured .sec-title{color:var(--white);margin-top:80px}
.work{position:absolute;top:1040px}
.work-a{left:272px;width:300px;height:368px;background:linear-gradient(135deg,#cfe5f3,#5b94c7 55%,#1d4e86)}
.work-b{left:584px;width:216px;height:170px;background:linear-gradient(135deg,#2a1856,#b43a6d 55%,#f08a3c)}
.work-c{left:584px;top:1222px;width:216px;height:186px;background:linear-gradient(135deg,#e6ecf2,#8b97a6 60%,#4e5866)}
.work-d{left:812px;width:228px;height:170px;background:linear-gradient(135deg,#b7c4d2,#3b4c63 70%)}
.work-e{left:812px;top:1222px;width:228px;height:186px;background:radial-gradient(circle at 50% 40%,#fff3c9,#7a8ea4 45%,#1a2a40)}

/* expertise */
.expertise{left:0;top:1440px;width:1200px;height:400px;background:linear-gradient(180deg,#eef4fa 0%,#d9e7f3 50%,#f4f8fc 100%)}
.expertise .sec-title{color:var(--navy);margin-top:150px}
.expertise .body-copy{width:880px;margin:26px auto 0}

/* clients */
.clients{left:0;top:1820px;width:1200px;height:480px;background:linear-gradient(180deg,#0e2f63,#123d7a 50%,#0c2c5c)}
.clients .sec-title{color:var(--white);margin-top:28px}
.client-grid{position:absolute;left:160px;top:100px;display:grid;grid-template-columns:repeat(5,152px);grid-auto-rows:120px;gap:20px 30px}
.client{display:flex;align-items:center;justify-content:center;gap:8px;border:3px solid var(--white);font-weight:700;font-size:17px}
.client i{display:block;width:12px;height:12px;background:currentColor}

/* approach */
.approach{left:0;top:2280px;width:1200px;height:600px;background:linear-gradient(180deg,#dbe9f5,#a9c9e6 60%,#e9f2fa)}
.approach .sec-title{color:var(--navy);margin-top:120px}
.approach-grid{position:absolute;left:160px;top:200px;display:grid;grid-template-columns:repeat(4,220px);grid-auto-rows:170px}
.tile-text{background:var(--deep);color:var(--white);padding:16px 18px}
.tile-text h3{font-size:14px;font-weight:700;margin-bottom:8px}
.tile-text p{font-size:11px;line-height:1.55;color:#dce8f5}
.tile-text .more{display:block;margin-top:8px;font-size:11px;font-weight:600;color:var(--white)}
.tile-img{width:220px;height:170px}

/* footer */
.footer{left:0;top:2880px;width:1200px;height:200px;background:#f5f8fb}
.footer .logo{position:absolute;left:240px;top:48px}
.footer .logo-mark{width:40px;height:40px}
.footer .logo-name{font-size:24px}
.f-col{position:absolute;top:34px}
.f-col h4{font-size:13px;font-weight:700;color:var(--navy);margin-bottom:10px;letter-spacing:1px}
.f-col li{list-style:none;font-size:11px;line-height:1.7;color:var(--muted)}
.f-col li::before{content:"› ";color:var(--deep)}
.f-col p{font-size:11px;line-height:1.7;color:var(--muted)}
.socials{display:flex;gap:6px;margin-top:8px}
.socials span{width:20px;height:20px;background:var(--mid)}
.news-input{width:160px;height:26px;border:1px solid var(--pale);background:var(--white);font-size:11px;color:var(--muted);padding:5px 8px;margin-top:8px}
.news-btn{display:inline-block;margin-top:8px;background:var(--deep);color:var(--white);font-size:11px;font-weight:700;padding:6px 14px}
.bottombar{left:0;top:3080px;width:1200px;height:52px;background:var(--navy);color:#a9bfd8;font-size:11px;display:flex;align-items:center;justify-content:center}
</style>
</head>
<body>

<div class="abs topbar">
  <span><svg width="12" height="12" viewBox="0 0 24 24"><path fill="#cfe0f3" d="M6.6 10.8c1.4 2.8 3.8 5.1 6.6 6.6l2.2-2.2c.3-.3.7-.4 1-.2 1.1.4 2.3.6 3.6.6.6 0 1 .4 1 1V20c0 .6-.4 1-1 1C10.6 21 3 13.4 3 4c0-.6.4-1 1-1h3.5c.6 0 1 .4 1 1 0 1.3.2 2.5.6 3.6.1.3 0 .7-.2 1z"/></svg>Contact Info: +45 71 83 96 54</span>
  <span><svg width="13" height="10" viewBox="0 0 26 20"><rect x="1" y="1" width="24" height="18" fill="none" stroke="#cfe0f3" stroke-width="2"/><path d="M1 1l12 10L25 1" fill="none" stroke="#cfe0f3" stroke-width="2"/></svg>info@kelvaris.com</span>
</div>

<header class="abs header">
  <div class="logo">
    <span class="logo-mark"></span>
    <div><div class="logo-name">KELVARIS</div><div class="logo-tag">SUSTAINABLE SOLUTIONS</div></div>
  </div>
  <nav class="nav">
    <a class="active" href="#">HOME</a><a href="#">EXPERTISE</a><a href="#">APPROACH</a><a href="#">CLIENTS</a><a href="#">ABOUT</a><a href="#">CONTACT</a>
  </nav>
</header>

<section class="abs hero" role="img" aria-label="Rows of solar panels beneath a bright blue sky with wind turbines">
  <div class="hero-box">WE PROVIDE COMPLETE SERVICES THROUGHOUT THE PRODUCT DEVELOPMENT PROCESS</div>
  <svg class="hero-cut" width="1200" height="140" viewBox="0 0 1200 140"><path d="M0 140V70Q600 0 1200 60V140Z" fill="#ffffff"/></svg>
</section>

<section class="abs welcome">
  <h2 class="sec-title">WELCOME</h2>
  <p class="body-copy">Kelvaris is a development company working in green energy and sustainable development. We support clients through design, engineering, manufacturing and sourcing, both as consultants and with our own products. Our team combines technical depth with practical experience to turn early ideas into reliable, market ready solutions. From the first concept sketch to series production, we keep quality, cost and the environment in balance, so every project leaves a smaller footprint and a stronger business behind it.</p>
</section>

<section class="abs featured"><h2 class="sec-title">FEATURED WORK</h2></section>
<div class="abs work work-a" role="img" aria-label="Glass and steel industrial pipework in cool blue light"></div>
<div class="abs work work-b" role="img" aria-label="Glowing technical components in violet and orange light"></div>
<div class="abs work work-c" role="img" aria-label="Close-up of metal gears and machined parts"></div>
<div class="abs work work-d" role="img" aria-label="Precision machinery in a workshop"></div>
<div class="abs work work-e" role="img" aria-label="Hanging light bulbs glowing in the dark"></div>

<section class="abs expertise" role="img" aria-label="Faded background of solar panels under soft light">
  <h2 class="sec-title">EXPERTISE</h2>
  <p class="body-copy">Our expertise covers the whole chain of product development for solar and clean energy. We handle mechanical and electrical design, prototyping, testing and certification, and we manage suppliers and production partners across Europe and Asia. Each project gets one dedicated team, clear milestones and honest reporting, so our clients always know where they stand and what comes next on the road to a finished product.</p>
</section>

<section class="abs clients">
  <h2 class="sec-title">CLIENTS</h2>
  <div class="client-grid">
    <div class="client" style="background:#1b4fa0;color:#fff"><i></i>Norrvik</div>
    <div class="client" style="background:#f06a1c;color:#fff"><i></i>Casaforge</div>
    <div class="client" style="background:#fff;color:#0b3c91">Veltrano</div>
    <div class="client" style="background:#f7c51b;color:#b0151e">Stromvale</div>
    <div class="client" style="background:#1f4ea3;color:#fff">Lumoria</div>
    <div class="client" style="background:#d2222d;color:#fff">Netharbor</div>
    <div class="client" style="background:#111;color:#f39a1b"><i></i>Toolmere</div>
    <div class="client" style="background:#1c9a4d;color:#fff">Quenby</div>
    <div class="client" style="background:#1a66c7;color:#fff">Brightholm</div>
    <div class="client" style="background:#fff;color:#c8202f"><i></i>Saltwick</div>
  </div>
</section>

<section class="abs approach">
  <h2 class="sec-title">APPROACH</h2>
  <div class="approach-grid">
    <div class="tile-img" style="background:linear-gradient(135deg,#cfe9f5,#6aa9d6)" role="img" aria-label="Hands using a tablet with business charts"></div>
    <div class="tile-text"><h3>WE ARE ABOUT BUSINESS</h3><p>We treat every project as an investment and focus on results that pay off for our partners.</p><span class="more">Read More...</span></div>
    <div class="tile-img" style="background:linear-gradient(135deg,#e8eef4,#9fb3c6)" role="img" aria-label="Bright modern kitchen interior"></div>
    <div class="tile-text"><h3>Minimum Viable Product</h3><p>We build the simplest working version first, test it early and improve it step by step.</p><span class="more">Read More...</span></div>
    <div class="tile-text"><h3>We Love Collaboration:</h3><p>Close teamwork with clients and suppliers keeps ideas moving and decisions quick and clear.</p><span class="more">Read More...</span></div>
    <div class="tile-img" style="background:linear-gradient(135deg,#d6dde5,#7d8ea1)" role="img" aria-label="Team of colleagues giving thumbs up"></div>
    <div class="tile-text"><h3>Taking Responsibility</h3><p>We own our work from start to finish and stand behind every part we deliver.</p><span class="more">Read More...</span></div>
    <div class="tile-img" style="background:linear-gradient(135deg,#eef1f4,#5d6f84)" role="img" aria-label="Two business people shaking hands"></div>
  </div>
</section>

<footer class="abs footer">
  <div class="logo">
    <span class="logo-mark"></span>
    <div><div class="logo-name">KELVARIS</div><div class="logo-tag">SUSTAINABLE SOLUTIONS</div></div>
  </div>
  <div class="f-col" style="left:520px">
    <h4>QUICK LINK</h4>
    <ul><li>HOME</li><li>EXPERTISE</li><li>APPROACH</li><li>CLIENTS</li><li>ABOUT</li><li>CONTACT</li></ul>
  </div>
  <div class="f-col" style="left:640px;width:220px">
    <h4>CONTACT INFO</h4>
    <p>Address: Havnestien 18, 2<br>DK-5820 Svendborg, Denmark</p>
    <p>Phone: +45 71 83 96 54</p>
    <p>Email: frederik.lysgaard@kelvaris.dk</p>
    <div class="socials"><span></span><span></span><span></span><span></span><span></span></div>
  </div>
  <div class="f-col" style="left:880px">
    <h4>NEWSLETTER</h4>
    <p>Sign up for Our Newsletter</p>
    <div class="news-input">Email address</div>
    <span class="news-btn">SUBSCRIBE</span>
  </div>
</footer>

<div class="abs bottombar">Copyright © 2016 Kelvaris. All Rights Reserved.</div>

</body>
</html>
```